Package design for quilted mattress covers.

We are producing a comfortable "quilted mattress protector" for beds . We need a very elegant and attractive and cozy insert label. approx. size is 14 inches high x11 inches wide. (One base design with slight edits to customize for each different bed size) It will be packaged in a nice clear bag, with the design label in front. I attached the type of product for reference

package text:
QUILTED MATTRESS COVER

size: 33x75x10"

*ultimate comfort
*breathable cotton top
*waterproof lining
*easy care wash and dry
Updates

Target Market(s)

displayed in drygood and bedding retail stores

Colors

Designer to choose colors to be used in the design.

Requirements
Must have
• all info as in description
Nice to have
• an image of a quilted cover on a bed, professionally included in the package design
Should not have
• ..

```html
<!DOCTYPE html>
<html lang="en">
<head>
<meta charset="utf-8">
<title>Lumora Quilted Mattress Cover – Package Label</title>
<link rel="stylesheet" href="https://fonts.googleapis.com/css2?family=Arimo:wght@400;700&family=Open+Sans:wght@400;600;700&display=swap">
<style>
  :root {
    --page-bg: #ffffff;
    --brand-blue: #5b84c7;
    --brand-navy: #2f4f8f;
    --white: #ffffff;
    --ink: #1c1c1c;
    --photo-light: #f2f2f0;
    --photo-mid: #d9d9d6;
    --photo-dark: #b9b9b6;
  }
  * { box-sizing: border-box; margin: 0; padding: 0; }
  html, body { width: 1000px; height: 1200px; overflow: hidden; background: var(--page-bg); }
  .canvas { position: relative; width: 1000px; height: 1200px; }

  .label {
    position: absolute; left: 148px; top: 208px; width: 714px; height: 930px;
    overflow: hidden; font-family: "Open Sans", Arial, sans-serif; color: var(--white);
  }
  .label-photo {
    position: absolute; inset: 0;
    background: linear-gradient(180deg, var(--photo-dark) 0%, var(--photo-light) 22%, var(--photo-mid) 45%, var(--photo-light) 60%, var(--photo-mid) 85%, var(--photo-dark) 100%);
  }
  .label-shapes { position: absolute; inset: 0; }

  .brand-name {
    position: absolute; left: 28px; top: 48px;
    font-family: "Arimo", Arial, sans-serif; font-weight: 700; font-size: 44px;
    line-height: 52px; letter-spacing: -1px; color: var(--brand-navy);
  }
  .product-name {
    position: absolute; left: 30px; top: 104px;
    font-family: "Arimo", Arial, sans-serif; font-weight: 700; font-size: 17px;
    line-height: 20px; letter-spacing: 1px; color: var(--brand-navy);
  }

  .feature { position: absolute; font-size: 14px; line-height: 20px; color: var(--white); }

  .quality-badge-text {
    position: absolute; left: 14px; top: 648px; width: 100px; text-align: center;
    font-family: "Arimo", Arial, sans-serif; font-weight: 700; color: var(--white); line-height: 1;
  }
  .quality-badge-text .small { font-size: 8px; display: block; }
  .quality-badge-text .big { font-size: 19px; display: block; margin: 2px 0; }

  .benefits {
    position: absolute; left: 427px; top: 664px; width: 240px; list-style: none;
    font-family: "Arimo", Arial, sans-serif; font-weight: 700; font-size: 17.5px; line-height: 22px;
    text-transform: uppercase; letter-spacing: 0.3px;
  }
  .benefits li { padding-left: 14px; text-indent: -14px; }
  .benefits li::before { content: "• "; }

  .size-title { position: absolute; left: 224px; top: 774px; font-size: 17px; line-height: 22px; }
  .size-dims { position: absolute; left: 12px; top: 802px; font-size: 17px; line-height: 22px; }

  .care-heading {
    position: absolute; left: 35px; top: 854px; width: 95px; height: 53px;
    background: var(--white); border-radius: 10px; color: var(--brand-blue);
    font-family: "Arimo", Arial, sans-serif; font-weight: 700; font-size: 15px; line-height: 18px;
    display: flex; align-items: center; justify-content: center; text-align: center;
  }
  .care-item {
    position: absolute; width: 70px; text-align: center;
    font-size: 7.5px; line-height: 9px; color: var(--white);
  }
</style>
</head>
<body>
<div class="canvas">
  <section class="label">
    <div class="label-photo" role="img" aria-label="Photo of a white quilted mattress cover on a bed with white pillows in a bright bedroom"></div>

    <svg class="label-shapes" width="714" height="930" viewBox="0 0 714 930">
      <path d="M552 0 L714 0 L714 930 L0 930 L0 802 C300 690 545 430 552 0 Z" fill="var(--brand-blue)"/>
      <line x1="0" y1="827" x2="714" y2="827" stroke="var(--white)" stroke-width="1.2" stroke-dasharray="4 3"/>
      <g stroke="var(--white)" stroke-width="1" stroke-dasharray="4 3">
        <line x1="254" y1="840" x2="254" y2="920"/>
        <line x1="367" y1="840" x2="367" y2="920"/>
        <line x1="472" y1="840" x2="472" y2="920"/>
        <line x1="582" y1="840" x2="582" y2="920"/>
      </g>

      <g transform="translate(64 672)">
        <circle r="52" fill="var(--brand-blue)" stroke="var(--white)" stroke-width="2" stroke-dasharray="3 3"/>
        <circle r="44" fill="none" stroke="var(--white)" stroke-width="1" stroke-dasharray="2 3"/>
      </g>

      <g fill="var(--white)" stroke="var(--brand-navy)" stroke-width="1.5">
        <circle cx="552" cy="202" r="26"/>
        <circle cx="538" cy="308" r="26"/>
        <circle cx="502" cy="392" r="26"/>
        <circle cx="450" cy="472" r="26"/>
        <circle cx="392" cy="537" r="26"/>
      </g>
      <g fill="var(--ink)">
        <path d="M552 188 l12 5 v9 c0 8 -6 12 -12 15 c-6 -3 -12 -7 -12 -15 v-9 z"/>
        <ellipse cx="538" cy="310" rx="9" ry="12"/>
        <g stroke="var(--ink)" stroke-width="2"><line x1="526" y1="302" x2="550" y2="318"/><line x1="526" y1="318" x2="550" y2="302"/><line x1="524" y1="310" x2="552" y2="310"/></g>
        <path d="M502 378 C496 388 492 394 492 399 a10 10 0 0 0 20 0 C512 394 508 388 502 378 Z"/>
        <path d="M436 480 a8 8 0 0 1 4 -14 a10 10 0 0 1 18 -2 a8 8 0 0 1 6 16 z"/>
        <path d="M392 524 l6 10 l8 -4 l-4 12 l-10 8 l-10 -8 l-4 -12 l8 4 z"/>
      </g>

      <g fill="none" stroke="var(--white)" stroke-width="1.5">
        <path d="M185 858 h28 l-3 22 h-22 z"/><path d="M188 864 q5 -3 10 0 t10 0"/>
        <path d="M310 858 l14 22 h-28 z"/><line x1="298" y1="858" x2="322" y2="880"/><line x1="322" y1="858" x2="298" y2="880"/>
        <rect x="406" y="856" width="24" height="24" rx="4"/><line x1="412" y1="868" x2="424" y2="868"/>
        <path d="M512 878 h26 v-20 h-16 q-8 0 -10 20 z"/><line x1="518" y1="864" x2="532" y2="864"/>
        <rect x="620" y="856" width="24" height="24"/><circle cx="632" cy="868" r="9"/><line x1="624" y1="860" x2="640" y2="876"/><line x1="640" y1="860" x2="624" y2="876"/>
      </g>
    </svg>

    <div class="brand-name">Lumora</div>
    <h1 class="product-name">QUILTED MATTRESS COVER</h1>

    <p class="feature" style="left:596px; top:180px;">100% bed<br>bug proof</p>
    <p class="feature" style="left:580px; top:286px;">100% dust<br>mite proof</p>
    <p class="feature" style="left:540px; top:384px;">Waterproof</p>
    <p class="feature" style="left:492px; top:450px;">Soft And<br>Comfortable</p>
    <p class="feature" style="left:430px; top:522px;">Naturally<br>Breathable</p>

    <div class="quality-badge-text">
      <span class="small">100%</span>
      <span class="big">QUALITY</span>
      <span class="small">GUARANTEED</span>
    </div>

    <ul class="benefits">
      <li>Ultimate comfort</li>
      <li>Breathable cotton top</li>
      <li>Waterproof lining</li>
      <li>Easy care wash and dry</li>
    </ul>

    <p class="size-title">Twin XL:</p>
    <p class="size-dims">39 inches wide x 80 inches long</p>

    <div class="care-heading">Care<br>Instrution</div>
    <div class="care-item" style="left:164px; top:893px;">Machine<br>Wash Warm</div>
    <div class="care-item" style="left:275px; top:893px;">Do Not<br>Bleach</div>
    <div class="care-item" style="left:383px; top:893px;">Tiled To<br>Dry</div>
    <div class="care-item" style="left:490px; top:893px;">Ironing At<br>Low Temp</div>
    <div class="care-item" style="left:597px; top:893px;">Do Not<br>Dry Clean</div>
  </section>
</div>
</body>
</html>
```